Luxury Wine Label for New Startup Winery

We need a wine label for our new winery startup. We have worked with a local designer but do not feel the resulting label / logo have the elevation required to present our brand as a luxury wine. Our winery is called "Harrowgate Vineyards" and we are focused on extremely high quality hand crafted artisan and estate wines from the Pacific Northwest.
We would like to see designs that utilize a tree line, or other imagery that represents the "Harrowgate" part of our company name. Another interesting feature could be wood grain.
A logo will be required based on your design so please design with this in mind:
This logo should be consistent with the wine bottle label design, and should be representative of our high end exclusive wine while giving a sense of place (Oregon/ Pacific Northwest.)
I will supply an image of the design we received from our local designer, PLEASE NOTE: in general we do like wood grain and tree line concepts but feel the execution was poorly done.
ATTN: Logo design should be suitable for use on: Bottles (Red wine/rose/white wine), Bussiness cards, vehicle signage, business signage, etc
P.S.:
If you have a design that is not outside the box we are still interested in seeing it.
Label is for a burgundy style bottle with a label height of 3.5 - 4" and a width of 3.5-4"
any label <= 4"x4" and >=3.5"x3.5" will be acceptable:
HOWEVER Width should be greater than or equal to height due to the bottle format
Target Market(s)
Wine enthusiasts with adequate discretionary budgets to afford $100 bottles of wine.
Industry/Entity Type
Wine / Winery
Requirements
Must have
- A sense of luxury, a feel of exclusivity, and a theme consistent with our product and brand name
Nice to have
- Tree line, wood grain or other wood themes. Serif fonts
Should not have
- anything cheesy, off topic, hard to read script fonts or anything that makes the label hard to read from a few feet away or too busy

```html
<!DOCTYPE html>
<html lang="en">
<head>
<meta charset="utf-8">
<title>Harrowgate Vineyards – Syrah Label</title>
<link rel="stylesheet" href="https://fonts.googleapis.com/css2?family=Cinzel:wght@400;600&family=Montserrat:wght@400&display=swap">
<style>
  :root {
    --bg: #000000;
    --ink-white: #ffffff;
    --label-black: #101211;
    --gold: #d9b04a;
    --gold-light: #f1d77a;
    --gold-deep: #a9802a;
    --silver: #cfd2d4;
    --silver-dark: #7c8083;
    --vine-grey: #b9bcbe;
    --wood-dark: #3a2414;
    --wood-mid: #5a3a22;
    --wood-light: #6e4a2c;
    --cream: #efe6d2;
  }
  * { margin: 0; padding: 0; box-sizing: border-box; }
  html, body { width: 1200px; height: 1200px; overflow: hidden; background: var(--bg); }
  .canvas { position: relative; width: 1200px; height: 1200px; background: var(--bg); }

  /* Brand logo (top left) */
  .brand-logo {
    position: absolute; left: 115px; top: 70px; width: 485px;
    text-align: center; color: var(--ink-white);
  }
  .brand-logo__name {
    font-family: "Cinzel", serif; font-weight: 600;
    font-size: 68px; line-height: 1; letter-spacing: 0.5px;
  }
  .brand-logo__sub {
    font-family: "Cinzel", serif; font-weight: 400;
    font-size: 25px; line-height: 1; letter-spacing: 19px; margin-top: 8px; padding-left: 19px;
  }

  /* Label */
  .label { position: absolute; left: 199px; top: 703px; width: 317px; }
  .label--on-bottle {
    left: 688px; top: 745px;
    transform: scale(0.69); transform-origin: top left;
    opacity: 0.92;
  }
  .label__main { position: relative; height: 257px; background: var(--label-black); }
  .label__rule {
    position: absolute; left: 10px; right: 10px; height: 2px;
    background: linear-gradient(90deg, var(--silver-dark), var(--silver), var(--silver-dark));
  }
  .label__rule--top { top: 4px; }
  .label__rule--top2 { top: 8px; height: 1px; }
  .label__rule--bottom { bottom: 8px; height: 1px; }
  .label__rule--bottom2 { bottom: 4px; }
  .label__treeline {
    position: absolute; left: 0; top: 20px; width: 317px; height: 90px;
    background: linear-gradient(180deg, rgba(217,176,74,0) 0%, rgba(217,176,74,0.25) 40%, rgba(217,176,74,0.75) 75%, var(--gold-light) 100%);
  }
  .label__wave { position: absolute; left: 0; top: 92px; width: 317px; height: 40px; }
  .label__name {
    position: absolute; left: 0; right: 0; top: 136px; text-align: center;
    font-family: "Cinzel", serif; font-weight: 600; font-size: 33px; line-height: 1;
    color: var(--gold);
  }
  .label__sub {
    position: absolute; left: 0; right: 0; top: 172px; text-align: center;
    font-family: "Cinzel", serif; font-size: 13px; line-height: 1; letter-spacing: 9px; padding-left: 9px;
    color: var(--vine-grey);
  }
  .label__region {
    position: absolute; left: 0; right: 0; top: 218px; text-align: center;
    font-family: "Montserrat", sans-serif; font-size: 12px; line-height: 1; letter-spacing: 0.5px;
    color: var(--gold);
  }
  .label__varietal-band {
    position: relative; margin-top: 9px; height: 70px;
    background: linear-gradient(180deg, var(--wood-mid) 0%, var(--wood-dark) 40%, var(--wood-light) 70%, var(--wood-dark) 100%);
  }
  .label__gold-line {
    position: absolute; left: 10px; right: 10px; height: 2px;
    background: linear-gradient(90deg, var(--gold-deep), var(--gold-light), var(--gold-deep));
  }
  .label__gold-line--top { top: 4px; }
  .label__gold-line--bottom { bottom: 4px; }
  .label__varietal {
    position: absolute; left: 0; right: 0; top: 17px; text-align: center;
    font-family: "Cinzel", serif; font-size: 18px; line-height: 1; color: var(--cream);
  }
  .label__vintage {
    position: absolute; left: 0; right: 0; top: 41px; text-align: center;
    font-family: "Cinzel", serif; font-size: 10px; line-height: 1; letter-spacing: 5px; padding-left: 5px;
    color: var(--cream);
  }
</style>
</head>
<body>
<main class="canvas">
  <header class="brand-logo">
    <div class="brand-logo__name">HARROWGATE</div>
    <div class="brand-logo__sub">VINEYARDS</div>
  </header>

  <section class="label">
    <div class="label__main">
      <div class="label__rule label__rule--top"></div>
      <div class="label__rule label__rule--top2"></div>
      <div class="label__treeline" role="img" aria-label="Gold foil evergreen tree line"></div>
      <svg class="label__wave" viewBox="0 0 317 40" preserveAspectRatio="none" aria-hidden="true">
        <defs>
          <linearGradient id="silverWaveA" x1="0" y1="0" x2="1" y2="0">
            <stop offset="0" stop-color="#8a8e91"/>
            <stop offset="0.35" stop-color="#f2f3f4"/>
            <stop offset="0.7" stop-color="#9da1a4"/>
            <stop offset="1" stop-color="#e6e8e9"/>
          </linearGradient>
        </defs>
        <path d="M0 12 C70 2 120 22 180 24 C240 26 280 14 317 16 L317 30 C280 28 240 40 180 38 C120 36 70 18 0 26 Z" fill="url(#silverWaveA)"/>
      </svg>
      <div class="label__name">HARROWGATE</div>
      <div class="label__sub">VINEYARDS</div>
      <div class="label__region">WILLAMETTE VALLEY</div>
      <div class="label__rule label__rule--bottom"></div>
      <div class="label__rule label__rule--bottom2"></div>
    </div>
    <div class="label__varietal-band" role="img" aria-label="Dark wood grain band">
      <div class="label__gold-line label__gold-line--top"></div>
      <div class="label__varietal">SYRAH</div>
      <div class="label__vintage">ESTATE | 2023 | GROWN</div>
      <div class="label__gold-line label__gold-line--bottom"></div>
    </div>
  </section>

  <section class="label label--on-bottle">
    <div class="label__main">
      <div class="label__rule label__rule--top"></div>
      <div class="label__rule label__rule--top2"></div>
      <div class="label__treeline" role="img" aria-label="Gold foil evergreen tree line"></div>
      <svg class="label__wave" viewBox="0 0 317 40" preserveAspectRatio="none" aria-hidden="true">
        <defs>
          <linearGradient id="silverWaveB" x1="0" y1="0" x2="1" y2="0">
            <stop offset="0" stop-color="#8a8e91"/>
            <stop offset="0.35" stop-color="#f2f3f4"/>
            <stop offset="0.7" stop-color="#9da1a4"/>
            <stop offset="1" stop-color="#e6e8e9"/>
          </linearGradient>
        </defs>
        <path d="M0 12 C70 2 120 22 180 24 C240 26 280 14 317 16 L317 30 C280 28 240 40 180 38 C120 36 70 18 0 26 Z" fill="url(#silverWaveB)"/>
      </svg>
      <div class="label__name">HARROWGATE</div>
      <div class="label__sub">VINEYARDS</div>
      <div class="label__region">WILLAMETTE VALLEY</div>
      <div class="label__rule label__rule--bottom"></div>
      <div class="label__rule label__rule--bottom2"></div>
    </div>
    <div class="label__varietal-band" role="img" aria-label="Dark wood grain band">
      <div class="label__gold-line label__gold-line--top"></div>
      <div class="label__varietal">SYRAH</div>
      <div class="label__vintage">ESTATE | 2023 | GROWN</div>
      <div class="label__gold-line label__gold-line--bottom"></div>
    </div>
  </section>
</main>
</body>
</html>
```